Stratgem 840 practise with the goal to have business and people empowered by the cloud

We need a logo design for business cards for a company based in Australia Called DUVOrbaLex. We specialise in cloud tech from th full Calventra stack. i would like it to be close to calventra colours and we specilise in Calventra Stratagem 840 Client Bondwork. the design should display the confidence an security of a cloud based company. the tag line of Empowered by the cloud in the company motto.

Target Market(s)

I am targeting small to medium business up to 250 staff. i do work for not for profit and standard business.

Industry/Entity Type

Professional Service

Contact Information for Business Card

DUVOrbaLex Pty Ltd
A.C.N. 47 918 264 530
PO Box 817
Brenthaven 4287
Mobile: 0499382057
Email: Bertram@DuvorbaLex.com.au

Font styles to use
Sans Serif

Colors

Designer to choose colors to be used in the design.

Requirements
Must have
• as a cloud based business it needs to have the this as the main theme. the tag line of Empoweredby the cloud should show we look at empowering business to get the most out of the cloud to minimise the spend they have as the target for the business is business and not for profits who need the make the most of their spend.
• the attached pictures are to be a source of insperation and key areas
Nice to have
• Calventra Stratagem 840 is the core product that we sell and implentent for our clients so the theme should complement the Calventra Stratagem theme

```html
<!DOCTYPE html>
<html lang="en">
<head>
<meta charset="utf-8">
<title>DUVOrbaLex Business Card</title>
<link rel="stylesheet" href="https://fonts.googleapis.com/css2?family=Outfit:wght@400;500&display=swap">
<style>
  :root {
    --page-bg: #cfcfcf;
    --card-bg: #e6e6e6;
    --accent-band: #6d82b0;
    --panel-navy: #3b4a69;
    --brand-navy: #1b2a78;
    --panel-text: #eef0f5;
  }
  html, body {
    margin: 0;
    padding: 0;
    width: 1200px;
    height: 1200px;
    overflow: hidden;
    background: var(--page-bg);
    font-family: "Outfit", sans-serif;
  }
  .canvas {
    position: relative;
    width: 1200px;
    height: 1200px;
  }
  .card {
    position: absolute;
    left: 254px;
    width: 690px;
    height: 394px;
    display: block;
  }
  .card--front { top: 175px; }
  .card--back { top: 597px; }
  .card-surface { fill: var(--card-bg); }
  .accent-band { fill: var(--accent-band); }
  .info-panel { fill: var(--panel-navy); }
  .brand-mark { fill: var(--brand-navy); }
  .brand-name {
    fill: var(--brand-navy);
    font-family: "Outfit", sans-serif;
    font-weight: 500;
    font-size: 40px;
  }
  .company-name {
    fill: var(--panel-text);
    font-family: "Outfit", sans-serif;
    font-weight: 400;
    font-size: 21px;
  }
  .contact-line {
    fill: var(--panel-text);
    font-family: "Outfit", sans-serif;
    font-weight: 400;
    font-size: 16.5px;
  }
</style>
</head>
<body>
<main class="canvas">

  <svg class="card card--front" viewBox="0 0 863 493" aria-label="Business card front">
    <rect class="card-surface" width="863" height="493"/>
    <polygon class="accent-band" points="0,0 560,0 490,47"/>
    <polygon class="accent-band" points="0,493 490,446 560,493"/>
    <g class="brand-lockup">
      <circle class="brand-mark" cx="282" cy="252" r="18"/>
      <text class="brand-name" x="318" y="266">DUVOrbaLex</text>
    </g>
  </svg>

  <svg class="card card--back" viewBox="0 0 863 493" aria-label="Business card back">
    <rect class="card-surface" width="863" height="493"/>
    <polygon class="info-panel" points="560,0 863,0 863,493 560,493 490,447 457,446 431,234 460,50 490,47"/>
    <polygon class="accent-band" points="0,0 560,0 490,47"/>
    <polygon class="accent-band" points="0,493 490,446 560,493"/>
    <g class="brand-lockup">
      <circle class="brand-mark" cx="70" cy="238" r="18"/>
      <text class="brand-name" x="106" y="252">DUVOrbaLex</text>
    </g>
    <g class="contact-block">
      <text class="company-name" x="513" y="174">DUVOrbaLex Pty Ltd</text>
      <text class="contact-line" x="513" y="216">A.C.N. 47 918 264 530</text>
      <text class="contact-line" x="513" y="237">PO Box 817</text>
      <text class="contact-line" x="513" y="259">Brenthaven 4287</text>
      <text class="contact-line" x="513" y="302">Mobile: 0499382057</text>
      <text class="contact-line" x="513" y="324">Email: Bertram@DuvorbaLex.com.au</text>
    </g>
  </svg>

</main>
</body>
</html>
```